Marrowind Vodka logo and label design

We would like a logo and bottle label design for a new line of Ultra-Premium Vodka. The Company is called Marrowind Spirits and is based in Brisbane, Australia. We would like a 'Gatsby/Prohibition era vibe to the design. We want to keep it minimalistic and sleek. We strongly prefer a minimalist design and colour palette. Black,Gold,Grey,White,Silver,Red and Blue

The bottle will be similar in shape to Halvorak/Pale Heron. There will also need to be space on the label for required information, as well as short bio of the company, which will be provided to the winning design.

We would like to add the polish code of arms for Opoczno. Have attached link for reference. https://www.crestarchive-demo.net/crestarchive/index.php?title=Opoczno

Target Market(s)

Luxury brand customers

Logo Text

Marrowind Ultra-Premium Vodka

Logo styles of interest
Wordmark Logo
Lettermark Logo
Requirements
Must have
• This is the first release from our new Vodka label. We want a logo and bottle label that reflects a premium product. We very much like Prohibition/Gatsby era themed bottles and labels. The label and bottle should be elegant and clean.
Should not have
• Anything too busy or confusing.

```html
<!DOCTYPE html>
<html lang="en">
<head>
<meta charset="utf-8">
<title>Marrowind Ultra Premium Vodka – Label</title>
<link rel="stylesheet" href="https://fonts.googleapis.com/css2?family=Jost:wght@500;600&display=swap">
<style>
  :root {
    --backdrop: #2a2b2d;
    --label-fill: #8f8f8f;
    --label-ink: #ffffff;
  }
  html, body {
    margin: 0;
    padding: 0;
    width: 1200px;
    height: 2400px;
    overflow: hidden;
    background: var(--backdrop);
  }
  .canvas {
    width: 1200px;
    height: 2400px;
    display: block;
  }
  .label-shape {
    fill: var(--label-fill);
    stroke: var(--label-ink);
    stroke-width: 17;
    stroke-linejoin: miter;
  }
  .label-text {
    fill: var(--label-ink);
    font-family: "Jost", "Futura", sans-serif;
    font-weight: 500;
    text-anchor: middle;
  }
  .brand-line { font-size: 67px; letter-spacing: 0.01em; }
  .product-name { font-size: 126px; letter-spacing: 0.13em; }
  .brand-mark { font-size: 40px; letter-spacing: 0.12em; }
  .vintage { font-size: 36px; letter-spacing: 0.04em; }
</style>
</head>
<body>
  <svg class="canvas" viewBox="0 0 1200 2400" xmlns="http://www.w3.org/2000/svg" role="img" aria-label="Marrowind Ultra Premium Vodka bottle label">
    <polygon class="label-shape"
      points="434,676 766,676 1010,957 1010,1448 766,1724 434,1724 190,1448 190,957"/>
    <text class="label-text brand-line" x="600" y="967">MARROWIND</text>
    <text class="label-text brand-line" x="600" y="1063">ULTRA</text>
    <text class="label-text brand-line" x="600" y="1157">PREMIUM</text>
    <text class="label-text product-name" x="613" y="1313">VODKA</text>
    <text class="label-text brand-mark" x="604" y="1509">MARROWIND</text>
    <text class="label-text vintage" x="600" y="1692">- 2021 -</text>
  </svg>
</body>
</html>
```